Chai Tea Company needs a Tea Packaging Box Design

Tea Packaging
Dimensions of the Tea Packaging Box: Height 13 cm; Width 8.5 cm; Depth 7 cm
Individual Teabag Packet/ Sachet: Width 6.5 cm; Length 8.25 cm
We are looking for a new tea packaging design, for our tea business. The material of the box is cardboard. We are also looking for a design that will be on each individual tea bag sachet/packet that goes into the box. This design will be very similar to what you design for the tea packaging box.
Product Info:
Our tea company is called “Velmora Leaf”. We sell two types of Chai Tea, once called “Velmora Gold” and one called “Velmora Bloom”. The Velmora Gold has caffeine, while the Velmora Bloom is Naturally Caffeine Free. The Velmora Gold has a black tea base, while the Velmora Bloom has a Rooibos tea base. We will need two tea packaging designs, one for each Chai Tea flavour. The designs for both the teas can be similar, but make sure that you can easily distinguish one from the other (example: make them have different colours or pictures). Both the chai teas, come from the same product line.
Tea Packaging Design:
We are looking for high end tea packaging. We produce high quality teas, and we would like to portray this in our tea packaging. Our teas are made with no artificial flavourings, natural flavourings, or preservatives, so we would also like a natural, organic, high quality look to our tea packaging. Our current logo is a llama. It would be great if you could make the current logo more polished and well made. If you feel that the llama is not well suited or you would like to design the llama differently, we are open to your creative ideas.
General Basic Info:
Keep in mind, we will have both English and French writing on the tea packaging. You do not need to worry about the French writing (we will do the translation), just make sure there is room for it. However, if you feel that you are capable and knowledgeable of incorporating both French and English language into the tea packaging that would be of great help and value.
Back of the Box:
- Will have ingredients and brewing instructions. Basic brewing instructions are: “Add hot water to teabag. Steep for 5-7 minutes, depending on strength preferred. Add milk and your choice of sweetener. Enjoy! See inside panel of box for more detailed instructions”. (The basic brewing instructions, can further be polished or written in a more creative or professional manner).
Front of the Box:
- Will have company name, type of tea, little description of the tea
- 18 teabags
- 54 g (1.9 OZ)
- Should state that this is a product of Alberta, Canada.
Side of the Box:
Any creative wording, slogan, or description about the tea, or whatever you feel would be good on the side of the box.
On the inside flap of the side of the box, there will be detailed instructions on how to brew the tea. These will be different from the simplified brewing instructions on the back of the box. I have attached the advanced brewing instructions as a file. These instructions can further be simplified or reduced to make it easier and cleaner for the consumers to read.
Individual Tea Sachets/ Packets
- These will have a matching look and design of the tea box packaging, except on a smaller scale. Each individual sachet will have the company name, type of tea, little description of the tea in the front of the sachet, while the back will contain the ingredients, and basic brewing instructions.
I have attached a few files, with the dimensions, ingredients, detailed brewing directions, and current logo of the business.
If you have any questions, about the design or packaging please let me know. The winning designer will be required to do a few additional tweaks to finalize the product. Thank you for your time and happy designing!

```html
<!DOCTYPE html>
<html lang="en">
<head>
<meta charset="utf-8">
<title>Velmora Leaf — Tea Packaging</title>
<link rel="stylesheet" href="https://fonts.googleapis.com/css2?family=Lobster+Two:ital,wght@0,700;1,700&family=Abril+Fatface&family=Oswald:wght@300&family=Signika:wght@400;600&display=swap">
<style>
  :root {
    --kraft-yellow: #f3c430;
    --kraft-yellow-deep: #e9b624;
    --spice-brown: #6a4716;
    --bloom-orange: #e8951c;
    --band-light: #f6cf4a;
    --paper: #ffffff;
  }
  * { box-sizing: border-box; margin: 0; padding: 0; }
  html, body { width: 1200px; height: 1000px; overflow: hidden; background: var(--paper); }
  body { position: relative; font-family: "Signika", sans-serif; color: var(--spice-brown); }

  /* Brand lockup: plain square beside the name in the text font */
  .brand { position: absolute; top: 110px; left: 0; width: 1200px; display: flex; justify-content: center; align-items: center; gap: 16px; }
  .brand-mark { display: block; width: 34px; height: 34px; background: var(--spice-brown); }
  .brand-name { font-family: "Signika", sans-serif; font-weight: 600; font-size: 34px; letter-spacing: 1px; color: var(--spice-brown); line-height: 1; }

  /* Box panels */
  .panel { position: absolute; top: 250px; height: 400px; background: var(--kraft-yellow); overflow: hidden; }
  .panel.side { width: 112px; background: var(--kraft-yellow-deep); }
  .panel.back { width: 290px; }
  .band { position: absolute; left: 0; width: 100%; height: 26px; }
  .band.top { top: 0; } .band.bottom { bottom: 0; }
  .bloom .band { background: linear-gradient(90deg, var(--band-light), var(--bloom-orange) 50%, var(--band-light)); border-bottom: 3px solid var(--spice-brown); }
  .bloom .band.bottom { border-bottom: 0; border-top: 3px solid var(--spice-brown); }
  .gold .band { background: linear-gradient(90deg, var(--spice-brown), #8a5c17 50%, var(--spice-brown)); }

  .back-body { position: absolute; top: 38px; left: 0; right: 0; text-align: center; }
  .serving { font-family: "Lobster Two", cursive; font-weight: 700; font-style: italic; font-size: 12px; }
  .heading { font-family: "Lobster Two", cursive; font-weight: 700; font-style: italic; font-size: 16px; line-height: 1.1; }
  .ingredients { list-style: none; font-size: 9.5px; font-weight: 600; line-height: 1.55; margin-top: 4px; }
  .rule { display: block; width: 70px; height: 3px; background: var(--spice-brown); border-radius: 2px; margin: 8px auto; opacity: .8; }
  .steps { list-style: none; text-align: left; margin: 6px 0 0 38px; font-size: 10.5px; font-weight: 600; }
  .steps li { display: flex; align-items: flex-start; gap: 7px; margin-bottom: 7px; line-height: 1.15; }
  .step-no { flex: none; width: 15px; height: 15px; border-radius: 50%; background: var(--spice-brown); color: var(--kraft-yellow); font-size: 9px; display: grid; place-items: center; }
  .note { font-size: 8px; font-weight: 600; margin-top: 4px; }
  .enjoy { font-family: "Lobster Two", cursive; font-weight: 700; font-size: 22px; margin-top: 8px; }

  .side-body { position: absolute; top: 36px; left: 8px; right: 8px; }
  .side-brand { font-family: "Signika", sans-serif; font-weight: 600; font-size: 10px; text-align: center; }
  .side-title { font-family: "Abril Fatface", serif; font-size: 24px; line-height: 1; margin-top: 22px; text-align: center; }
  .side-variety { font-family: "Oswald", sans-serif; font-weight: 300; font-size: 15px; letter-spacing: 3px; text-align: center; margin-top: 2px; }
  .side-copy { font-size: 8px; font-weight: 600; line-height: 1.4; margin-top: 14px; }
  .side-copy + .side-copy { margin-top: 8px; font-style: italic; }
  .bag-count { position: absolute; bottom: 34px; left: 0; right: 0; text-align: center; font-size: 9px; font-weight: 600; }

  /* Sachets */
  .sachet { position: absolute; top: 680px; width: 180px; height: 230px; background: var(--kraft-yellow); overflow: hidden; }
  .sachet-cap { position: absolute; left: 0; width: 100%; height: 46px; }
  .sachet-cap.top { top: 0; } .sachet-cap.bottom { bottom: 0; transform: scaleY(-1); }
  .sachet-body { position: absolute; top: 56px; left: 0; right: 0; text-align: center; }
  .sachet .heading { font-size: 13px; }
  .sachet .rule { width: 50px; margin: 5px auto; }
  .sachet .steps { margin-left: 14px; font-size: 9px; }
  .sachet .steps li { margin-bottom: 5px; }
  .sachet .step-no { width: 13px; height: 13px; font-size: 8px; }
</style>
</head>
<body>

<header class="brand">
  <span class="brand-mark"></span>
  <div class="brand-name">Velmora Leaf</div>
</header>

<!-- Velmora Bloom box -->
<section class="panel side bloom" style="left:168px">
  <div class="band top" role="img" aria-label="Floral pattern band"></div>
  <div class="side-body">
    <div class="side-brand">Velmora Leaf</div>
    <div class="side-title">Velmora</div>
    <div class="side-variety">BLOOM</div>
    <p class="side-copy">A caffeine free blend of rooibos and warming spices, with cardamom, cloves, fennel, ginger and cinnamon for a smooth cup.</p>
    <p class="side-copy">Un mélange sans caféine de rooibos et d'épices chaudes, cardamome, clous de girofle, fenouil, gingembre et cannelle.</p>
  </div>
  <div class="band bottom" role="img" aria-label="Floral pattern band"></div>
</section>

<section class="panel back bloom" style="left:280px">
  <div class="band top" role="img" aria-label="Floral pattern band"></div>
  <div class="back-body">
    <div class="serving">• For 2 Cups •</div>
    <div class="heading">Ingredients</div>
    <ul class="ingredients">
      <li>• 1 1/2 cups (12 oz) water •</li>
      <li>• 2 chai tea bags •</li>
      <li>• 1 cup (8 oz) (whole) milk •</li>
      <li>• 2-4 tsps sugar or honey •</li>
      <li>• 1-2 tsps of sliced or grated fresh ginger (optional) •</li>
    </ul>
    <span class="rule"></span>
    <div class="heading">Brewing Instructions</div>
    <span class="rule"></span>
    <ol class="steps">
      <li><span class="step-no">1</span>add hot water to tea bag</li>
      <li><span class="step-no">2</span>steep for 5-7 minutes -<br>depending on prefered strength</li>
      <li><span class="step-no">3</span>add milk</li>
      <li><span class="step-no">4</span>add your choice of sweetener</li>
    </ol>
    <p class="note">(see inside panel of box for more detailed instructions)</p>
    <span class="rule"></span>
    <div class="enjoy">Enjoy</div>
  </div>
  <div class="band bottom" role="img" aria-label="Floral pattern band"></div>
</section>

<!-- Velmora Gold box -->
<section class="panel back gold" style="left:630px">
  <div class="band top" role="img" aria-label="Floral pattern band on brown"></div>
  <div class="back-body">
    <div class="serving">• For 2 Cups •</div>
    <div class="heading">Ingredients</div>
    <ul class="ingredients">
      <li>• 1 1/2 cups (12 oz) water •</li>
      <li>• 2 chai tea bags •</li>
      <li>• 1 cup (8 oz) (whole) milk •</li>
      <li>• 2-4 tsps sugar or honey •</li>
      <li>• 1-2 tsps of sliced or grated fresh ginger (optional) •</li>
    </ul>
    <span class="rule"></span>
    <div class="heading">Brewing Instructions</div>
    <span class="rule"></span>
    <ol class="steps">
      <li><span class="step-no">1</span>add hot water to tea bag</li>
      <li><span class="step-no">2</span>steep for 5-7 minutes -<br>depending on prefered strength</li>
      <li><span class="step-no">3</span>add milk</li>
      <li><span class="step-no">4</span>add your choice of sweetener</li>
    </ol>
    <p class="note">(see inside panel of box for more detailed instructions)</p>
    <span class="rule"></span>
    <div class="enjoy">Enjoy</div>
  </div>
  <div class="band bottom" role="img" aria-label="Floral pattern band on brown"></div>
</section>

<section class="panel side gold" style="left:920px">
  <div class="band top" role="img" aria-label="Floral pattern band on brown"></div>
  <div class="side-body">
    <div class="side-brand">Velmora Leaf</div>
    <div class="side-title">Velmora</div>
    <div class="side-variety">GOLD</div>
    <p class="side-copy">A robust tea with cardamom, cloves, fennel, ginger and cinnamon.</p>
    <p class="side-copy">Un thé à la cardamome noire, clous de girofle, le fenouil, gingembre et la cannelle.</p>
  </div>
  <div class="bag-count">18 Tea Bags</div>
  <div class="band bottom" role="img" aria-label="Floral pattern band on brown"></div>
</section>

<!-- Sachets -->
<section class="sachet bloom" style="left:420px">
  <svg class="sachet-cap top" viewBox="0 0 180 46" preserveAspectRatio="none" role="img" aria-label="Floral pattern cap">
    <path d="M0 0H180V14Q90 60 0 14Z" fill="#e8951c"/>
    <path d="M0 14Q90 60 180 14" fill="none" stroke="#6a4716" stroke-width="3"/>
  </svg>
  <div class="sachet-body">
    <div class="heading">Brewing Instructions</div>
    <span class="rule"></span>
    <ol class="steps">
      <li><span class="step-no">1</span>add hot water to tea bag</li>
      <li><span class="step-no">2</span>steep for 5-7 minutes -<br>depending on prefered strength</li>
      <li><span class="step-no">3</span>add milk</li>
      <li><span class="step-no">4</span>add your choice of sweetener</li>
    </ol>
  </div>
  <svg class="sachet-cap bottom" viewBox="0 0 180 46" preserveAspectRatio="none" role="img" aria-label="Floral pattern cap">
    <path d="M0 0H180V14Q90 60 0 14Z" fill="#e8951c"/>
    <path d="M0 14Q90 60 180 14" fill="none" stroke="#6a4716" stroke-width="3"/>
  </svg>
</section>

<section class="sachet gold" style="left:610px">
  <svg class="sachet-cap top" viewBox="0 0 180 46" preserveAspectRatio="none" role="img" aria-label="Floral pattern cap on brown">
    <path d="M0 0H180V14Q90 60 0 14Z" fill="#6a4716"/>
  </svg>
  <div class="sachet-body">
    <div class="heading">Brewing Instructions</div>
    <span class="rule"></span>
    <ol class="steps">
      <li><span class="step-no">1</span>add hot water to tea bag</li>
      <li><span class="step-no">2</span>steep for 5-7 minutes -<br>depending on prefered strength</li>
      <li><span class="step-no">3</span>add milk</li>
      <li><span class="step-no">4</span>add your choice of sweetener</li>
    </ol>
  </div>
  <svg class="sachet-cap bottom" viewBox="0 0 180 46" preserveAspectRatio="none" role="img" aria-label="Floral pattern cap on brown">
    <path d="M0 0H180V14Q90 60 0 14Z" fill="#6a4716"/>
  </svg>
</section>

</body>
</html>
```